Flyer for an online formula one racing league

Hello.

I am looking for the perfect one page facebook/instagram style flyer for an online formula one racing league. The racing league is called 'VOLTA RACING LEAGUE'.

Information that MUST be on the new flyer is already on the old flyer I have uploaded here. In addition to including: The Volta racing league 'V' logo I have uploaded AND the text: 'Very popular, clean and competitive racing league, running for its 4th season. Why not join with a friend? Race times, Mondays, Tuesdays and Wednesdays each at 8pm UK TIME Message below for any questions. (Spacing of information is not important, however all the information in regards to the racing I have just mentioned MUST BE on the flyer, this includes info from old pic, logo and the other info I just mentioned).

It would be beneficial to have lots of dark blue on the flyer and the new flyer to be a lot different to the original flyer I uploaded, but this is not essential.

I apologise if I did not explain very well, any questions, please message me.

The best flyer should look the most attractive to someone that might be interested in joining an online formula one racing league.

I used this website before to create the perfect logo for my Sunday League team last year, and I was very impressed. I look forward to seeing your submissions.

Target Market(s)

No specific target, more something that may attract someone into joining a formula one online racing league

Industry/Entity Type

e sports/formula one

Colors
0054AA
0677BA
7BADD7
CADEEF
E8F1F8

Requirements
Must have
• Read product description please
Should not have
• Ignoring product description!

```html
<!DOCTYPE html>
<html lang="en">
<head>
<meta charset="utf-8">
<title>Volta Racing League – Season 4 Flyer</title>
<link href="https://fonts.googleapis.com/css2?family=Anton&family=Poppins:wght@600;700;800&family=Roboto+Condensed:wght@700;800&display=swap" rel="stylesheet">
<style>
  :root {
    --backdrop: #5b5b5b;
    --navy-deep: #0a0a5e;
    --navy: #0d14a8;
    --royal: #1a2bd6;
    --violet: #3b2fc4;
    --band: #0b0b6a;
    --band-line: #6f73ff;
    --yellow: #ffff00;
    --tag-yellow: #ffe600;
    --tag-orange: #f7a21b;
    --white: #ffffff;
    --silver: #c9ccd6;
    --crimson: #b3163f;
    --ink: #111111;
    --badge: #0d1030;
  }
  * { margin: 0; padding: 0; box-sizing: border-box; }
  html, body { width: 1200px; height: 1000px; overflow: hidden; background: var(--backdrop); }

  .flyer {
    position: absolute; left: 117px; top: 228px; width: 967px; height: 543px;
    overflow: hidden;
    background:
      radial-gradient(ellipse 260px 120px at 640px 300px, rgba(255,120,160,.45), transparent 70%),
      radial-gradient(ellipse 420px 200px at 560px 160px, rgba(255,170,90,.35), transparent 70%),
      linear-gradient(180deg, var(--navy-deep) 0%, var(--navy) 35%, var(--royal) 60%, var(--navy) 100%);
    box-shadow: 0 6px 14px rgba(0,0,0,.45);
  }
  .flyer__decor { position: absolute; inset: 0; }

  .gauge-art {
    position: absolute; left: 690px; top: 8px; width: 240px; height: 200px; border-radius: 50%;
    background: radial-gradient(circle at 55% 60%, rgba(220,40,90,.55), rgba(120,60,200,.25) 55%, transparent 72%);
  }

  .brand { position: absolute; left: 23px; top: 12px; width: 156px; height: 156px; border-radius: 50%;
    background: var(--badge); display: flex; align-items: center; justify-content: center; }
  .brand__name { font-family: 'Poppins', sans-serif; font-weight: 800; font-size: 30px; color: var(--white); letter-spacing: 1px; }

  .title { position: absolute; left: 0; width: 100%; font-family: 'Anton', sans-serif; text-transform: uppercase;
    color: var(--white); text-shadow: 3px 4px 0 #2b2b44, 0 0 18px rgba(255,255,255,.25); transform: skewX(-12deg); line-height: 1; }
  .title--top { top: 32px; left: 340px; width: auto; font-size: 80px; }
  .title--main { top: 108px; left: 203px; width: auto; font-size: 80px; letter-spacing: 1px; }
  .title span { background: linear-gradient(180deg, var(--white) 45%, var(--silver) 60%, var(--white) 100%);
    -webkit-background-clip: text; background-clip: text; color: transparent; }

  .season-tag { position: absolute; left: 712px; top: 193px; width: 156px; height: 28px;
    background: linear-gradient(90deg, var(--tag-yellow), var(--tag-orange)); transform: skewX(-22deg);
    display: flex; align-items: center; justify-content: center; }
  .season-tag__text { transform: skewX(22deg); font-family: 'Poppins', sans-serif; font-weight: 700; font-size: 19px; color: var(--ink); letter-spacing: .5px; }

  .tagline { position: absolute; left: 0; width: 100%; text-align: center; top: 230px;
    font-family: 'Poppins', sans-serif; font-weight: 700; font-size: 35px; color: var(--yellow); letter-spacing: .3px; }
  .tagline sup { font-size: 20px; vertical-align: 14px; }

  .launch-bar { position: absolute; left: 217px; top: 288px; width: 532px; height: 41px;
    background: linear-gradient(90deg, var(--tag-yellow) 40%, var(--tag-orange)); transform: skewX(-22deg);
    display: flex; align-items: center; justify-content: center; }
  .launch-bar__text { transform: skewX(22deg); font-family: 'Poppins', sans-serif; font-weight: 700; font-size: 26px; color: var(--ink); }

  .pitch { position: absolute; left: 0; width: 100%; text-align: center; font-family: 'Poppins', sans-serif; font-weight: 600; color: var(--white); }
  .pitch--lead { top: 346px; font-size: 28px; }
  .pitch--sub { top: 383px; font-size: 17px; font-weight: 700; }

  .schedule { position: absolute; left: 0; top: 424px; width: 100%; height: 119px;
    background: linear-gradient(180deg, rgba(11,11,106,.2), var(--band) 35%); }
  .schedule__line { position: absolute; left: 0; height: 4px; background: var(--band-line); }
  .schedule__line--top { top: 23px; width: 560px; }
  .schedule__line--bottom { top: 98px; width: 100%; height: 4px; opacity: .7; }
  .schedule__label { position: absolute; left: 0; width: 100%; text-align: center; top: 0px;
    font-family: 'Roboto Condensed', sans-serif; font-weight: 800; font-size: 40px; color: var(--yellow); }
  .schedule__days { position: absolute; left: 0; width: 100%; top: 42px; display: flex; justify-content: center; align-items: center; gap: 10px;
    font-family: 'Roboto Condensed', sans-serif; font-weight: 800; font-size: 57px; color: var(--white); line-height: 1; }
  .schedule__arrow { width: 28px; height: 36px; }
</style>
</head>
<body>
  <main class="flyer">
    <svg class="flyer__decor" width="967" height="543" viewBox="0 0 967 543" aria-hidden="true">
      <defs>
        <linearGradient id="chevronBlue" x1="0" x2="1"><stop offset="0" stop-color="#2a3cff" stop-opacity=".2"/><stop offset="1" stop-color="#2f47ff"/></linearGradient>
        <linearGradient id="chevronRed" x1="0" x2="1"><stop offset="0" stop-color="#8a1a5a" stop-opacity=".4"/><stop offset="1" stop-color="#b3163f"/></linearGradient>
        <linearGradient id="streak" x1="0" x2="1"><stop offset="0" stop-color="#fff" stop-opacity="0"/><stop offset=".5" stop-color="#ffd9a0"/><stop offset="1" stop-color="#fff" stop-opacity="0"/></linearGradient>
      </defs>
      <polygon points="170,0 250,0 320,70 250,140 170,140 240,70" fill="url(#chevronBlue)" opacity=".8"/>
      <polygon points="260,0 320,0 390,70 320,140 260,140 330,70" fill="url(#chevronBlue)"/>
      <polygon points="340,0 400,0 470,70 400,140 340,140 410,70" fill="url(#chevronRed)" opacity=".8"/>
      <polygon points="0,140 980,120 980,150 0,170" fill="#2c3cff" opacity=".25"/>
      <polygon points="0,290 300,280 300,330 0,340" fill="#3a4cff" opacity=".2"/>
      <polygon points="700,290 967,280 967,330 700,340" fill="#3a4cff" opacity=".2"/>
      <rect x="250" y="88" width="520" height="3" fill="url(#streak)"/>
      <rect x="330" y="150" width="420" height="2" fill="url(#streak)"/>
      <g fill="#ff7aa8" opacity=".7">
        <circle cx="60" cy="215" r="1.5"/><circle cx="120" cy="250" r="1.2"/><circle cx="210" cy="190" r="1.4"/>
        <circle cx="880" cy="220" r="1.5"/><circle cx="930" cy="260" r="1.2"/><circle cx="820" cy="380" r="1.5"/>
        <circle cx="60" cy="400" r="1.3"/><circle cx="840" cy="440" r="1.6"/><circle cx="500" cy="200" r="1.2"/>
      </g>
    </svg>

    <div class="gauge-art" role="img" aria-label="Glowing racing speedometer illustration"></div>

    <div class="brand"><span class="brand__name">VOLTA</span></div>

    <h1>
      <span class="title title--top"><span>Volta</span></span>
      <span class="title title--main"><span>Racing League</span></span>
    </h1>
    <div class="season-tag"><span class="season-tag__text">SEASON 4</span></div>

    <p class="tagline">RUNNING FOR IT’S 4<sup>TH</sup> YEAR</p>

    <div class="launch-bar"><span class="launch-bar__text">NEW SEASON JUST STARTING !!!</span></div>

    <p class="pitch pitch--lead">CLEAN ONLINE RACING LEAGUE</p>
    <p class="pitch pitch--sub">3 DIVISIONS CURRENTLY AND LOOKING TO KEEP GROWING!</p>

    <section class="schedule">
      <div class="schedule__line schedule__line--top"></div>
      <div class="schedule__line schedule__line--bottom"></div>
      <p class="schedule__label">SPACES LEFT ON</p>
      <div class="schedule__days">
        <span>MONDAYS</span>
        <svg class="schedule__arrow" viewBox="0 0 28 36" aria-hidden="true"><polygon points="0,0 12,0 28,18 12,36 0,36 16,18" fill="var(--crimson)"/></svg>
        <span>TUESDAYS</span>
        <svg class="schedule__arrow" viewBox="0 0 28 36" aria-hidden="true"><polygon points="0,0 12,0 28,18 12,36 0,36 16,18" fill="var(--crimson)"/></svg>
        <span>WEDNESDAYS</span>
      </div>
    </section>
  </main>
</body>
</html>
```